Flyer Design Project

Looking for a double sided DL flyer for distribution. (please see our generic corp flyer attached)

DL Size Flyer Flyer . Include bleed for printing. We have a printer.
Thinking a landscape format will work best.

We have an online business, http://www.kettlewomp.com.au

We are an online service that helps you organised your group gift collection. We take the process of collecting money from people and put it online. We provide the central payment point and communication platform.

Please watch http://www.vidplexo.com/watch?v=Q3rT7kLm2Xa

Target Market(s)

Parents of school age children

Industry/Entity Type

Communication

Requirements
Must have
• Font - calibri / lucinda sans unicode

The front side of the flyer would feature:

Heading ... Teacher end of Year Thank you
a teacher visual (attached)
logo (horizontal & vertical attached - you decide which fits best)
web address - www.kettlewomp.com.au

The back side of the flyer would feature:
copy (attached)
logo

please be mindful of our corporate colours (purple & green) and the look and feel of our website.

```html
<!DOCTYPE html>
<html lang="en">
<head>
<meta charset="utf-8">
<title>Kettlewomp – Teacher End of Year Thank you</title>
<link rel="stylesheet" href="https://fonts.googleapis.com/css2?family=Carlito:ital,wght@0,400;0,700;1,400;1,700&display=swap">
<style>
  :root {
    --purple-deep: #46265f;
    --purple-band: #552f73;
    --purple-light: #7a4f9a;
    --lime: #c9da2c;
    --lime-bright: #d4e23a;
    --cream: #fbf9f3;
    --ink: #2b2238;
    --white: #ffffff;
  }
  html, body {
    margin: 0;
    padding: 0;
    width: 1200px;
    height: 599px;
    overflow: hidden;
    background: var(--white);
  }
  .flyer {
    position: relative;
    width: 1200px;
    height: 599px;
    overflow: hidden;
    font-family: "Carlito", "Calibri", sans-serif;
    background: linear-gradient(180deg, var(--white) 0%, var(--cream) 45%, #efeee4 100%);
  }
  .band-purple {
    position: absolute;
    left: 0; top: 268px;
    width: 1200px; height: 166px;
    background: linear-gradient(180deg, var(--purple-light) 0px, var(--purple-band) 12px, var(--purple-deep) 100%);
  }
  .band-lime {
    position: absolute;
    left: 0; top: 434px;
    width: 1200px; height: 165px;
    background: linear-gradient(180deg, var(--lime-bright) 0%, var(--lime) 100%);
  }
  .brand {
    position: absolute;
    left: 30px; top: 58px;
    display: flex;
    align-items: center;
    gap: 18px;
  }
  .brand-dot {
    width: 86px; height: 86px;
    border-radius: 50%;
    background: var(--purple-band);
  }
  .brand-name {
    font-size: 62px;
    font-weight: 700;
    color: var(--purple-band);
    letter-spacing: -1px;
  }
  .photo {
    position: absolute;
    left: 742px; top: -92px;
    width: 468px; height: 468px;
    border-radius: 50%;
    border: 7px solid var(--purple-band);
    background: radial-gradient(circle at 60% 55%, #d9c2ab 0%, #a98a74 40%, #6c5a6e 75%, #4a3f5c 100%);
    box-sizing: border-box;
  }
  .ribbon {
    position: absolute;
    left: 520px; top: 175px;
    width: 300px; height: 410px;
    border-radius: 45% 45% 30% 30%;
    background: radial-gradient(ellipse at 50% 45%, rgba(122,79,154,0.85) 0%, rgba(85,47,115,0.55) 55%, rgba(85,47,115,0) 75%);
  }
  .headline {
    position: absolute;
    left: 40px; top: 274px;
    margin: 0;
    font-weight: 400;
  }
  .headline-main {
    display: block;
    font-size: 64px;
    font-weight: 700;
    font-style: italic;
    color: var(--lime);
    line-height: 1.05;
  }
  .headline-sub {
    display: block;
    font-size: 40px;
    font-style: italic;
    color: var(--white);
    margin-top: 6px;
  }
  .web {
    position: absolute;
    right: 34px; bottom: 20px;
    font-size: 21px;
    font-style: italic;
    color: var(--ink);
  }
</style>
</head>
<body>
  <main class="flyer">
    <div class="band-purple"></div>
    <div class="band-lime"></div>

    <div class="brand">
      <span class="brand-dot"></span>
      <span class="brand-name">Kettlewomp</span>
    </div>

    <div class="photo" role="img" aria-label="Photo of a smiling teacher in a classroom receiving apples from a student, world map behind"></div>

    <div class="ribbon" role="img" aria-label="Purple satin gift ribbon and bow"></div>

    <h1 class="headline">
      <span class="headline-main">Teacher</span>
      <span class="headline-sub">End of Year Thank you...</span>
    </h1>

    <p class="web">www.kettlewomp.com.au</p>
  </main>
</body>
</html>
```